Talbrin Business Cards

Front and back. Simon Kavelle MBA is the CEO of Talbrin Homes. Black white and grays. Logo and cool design.

Target Market(s)

Professional lenders and investors

Industry/Entity Type

Real estate developer. NO HOUSES OR ROOFS

Contact Information for Business Card

Logo, name and unique design. Front and back. Simon Kavelle MBA is the CEO of Talbrin Homes. Black white and grays. Logo and cool design.

Font styles to use
Sans Serif

Colors

Designer to choose only greyscale colors for use in the design.

Requirements
Must have
• Cool look. Not the same card I could design.
Nice to have
• Something memorable
Should not have
• Basic

```html
<!DOCTYPE html>
<html lang="en">
<head>
<meta charset="utf-8">
<title>Talbrin Homes Business Cards</title>
<link rel="stylesheet" href="https://fonts.googleapis.com/css2?family=Roboto:wght@400;500;700;900&display=swap">
<style>
  :root {
    --backdrop: #8c8c8c;
    --ink: #000000;
    --paper: #ffffff;
    --muted: #6f6f6f;
    --soft: #9a9a9a;
  }
  * { box-sizing: border-box; margin: 0; padding: 0; }
  html, body { width: 1200px; height: 1056px; overflow: hidden; }
  body {
    background: var(--backdrop);
    font-family: "Roboto", Arial, sans-serif;
    position: relative;
  }
  .card {
    position: absolute;
    left: 290px;
    width: 620px;
    height: 354px;
    box-shadow: 0 18px 30px rgba(0,0,0,0.28);
  }
  .card--front { top: 100px; background: var(--ink); }
  .card--back { top: 562px; background: var(--paper); }

  .wordmark {
    position: absolute;
    left: 0; right: 0;
    text-align: center;
    font-weight: 900;
    font-size: 60px;
    letter-spacing: -1px;
    line-height: 1;
  }
  .card--front .wordmark { top: 144px; color: var(--paper); }
  .card--back .wordmark { top: 66px; color: var(--ink); }

  .name-band {
    position: absolute;
    left: 0;
    top: 218px;
    width: 306px;
    height: 72px;
    background: var(--ink);
    border-top-right-radius: 10px;
    border-bottom-right-radius: 4px;
    text-align: right;
    padding: 12px 16px 0 0;
  }
  .name-band__name {
    color: var(--paper);
    font-weight: 700;
    font-size: 21px;
    line-height: 1.2;
  }
  .name-band__title {
    color: var(--muted);
    font-weight: 400;
    font-size: 15px;
    line-height: 1.3;
  }

  .contact-list {
    position: absolute;
    left: 318px;
    top: 190px;
    list-style: none;
  }
  .contact-list__item {
    display: flex;
    align-items: center;
    gap: 8px;
    height: 27px;
    color: var(--muted);
    font-size: 15px;
  }
  .contact-list__icon { width: 20px; height: 20px; flex: none; }
</style>
</head>
<body>

<section class="card card--front" aria-label="Card front">
  <div class="wordmark">Talbrin Homes</div>
</section>

<section class="card card--back" aria-label="Card back">
  <div class="wordmark">Talbrin Homes</div>

  <div class="name-band">
    <div class="name-band__name">Simon Kavelle MBA</div>
    <div class="name-band__title">CEO of Talbrin Homes</div>
  </div>

  <ul class="contact-list">
    <li class="contact-list__item">
      <svg class="contact-list__icon" viewBox="0 0 20 20" aria-hidden="true">
        <rect width="20" height="20" rx="4" fill="#000"/>
        <path d="M6 4.5c.6-.4 1.3-.3 1.7.3l1.1 1.7c.3.5.2 1.1-.2 1.5l-.8.7c.6 1.3 1.6 2.4 2.9 3l.7-.8c.4-.4 1-.5 1.5-.2l1.7 1.1c.6.4.7 1.1.3 1.7l-.6.8c-.6.7-1.6 1-2.5.6C8.7 13.6 6.4 11.3 5.1 8.2c-.4-.9-.1-1.9.6-2.5z" fill="#fff"/>
      </svg>
      <span>(000) 123-4567</span>
    </li>
    <li class="contact-list__item">
      <svg class="contact-list__icon" viewBox="0 0 20 20" aria-hidden="true">
        <rect width="20" height="20" rx="4" fill="#000"/>
        <rect x="4" y="6" width="12" height="8.5" rx="1" fill="none" stroke="#fff" stroke-width="1.4"/>
        <path d="M4.5 6.6 10 11l5.5-4.4" fill="none" stroke="#fff" stroke-width="1.4"/>
      </svg>
      <span>info@talbrinhomes.com</span>
    </li>
    <li class="contact-list__item">
      <svg class="contact-list__icon" viewBox="0 0 20 20" aria-hidden="true">
        <rect width="20" height="20" rx="4" fill="#000"/>
        <path d="M6 5l8 4-3.4 1.2 2.6 3.4-1.3 1-2.6-3.4L7.5 13.6z" fill="#fff"/>
      </svg>
      <span>www.talbrinhomes.com</span>
    </li>
  </ul>
</section>

</body>
</html>
```